Plumbing Business Letterhead Design

Need a letterhead designed to use for my invoices and letters. I would like it to incorporate my business logo, which i will upload, and use light blue and grey colours. Or any colours that will work well with my logo (im not very good with art to know) . Also the letterhead needs to include the following:
Address - P.O Box 4826 Bega NSW 2550
Email - gareth@rwhitfieldplumbing.example.au
ABN - 41 906 572 338
Licence No. - 582061K
Mobile - 0412076584

Industry/Entity Type

Plumbing

Font styles to use
Sans Serif

Colors

Designer to choose colors to be used in the design.

```html
<!DOCTYPE html>
<html lang="en">
<head>
<meta charset="utf-8">
<title>Gareth Whitfield Plumbing – Letterhead</title>
<link rel="stylesheet" href="https://fonts.googleapis.com/css2?family=Open+Sans:wght@400;600&display=swap">
<style>
  :root {
    --backdrop: #efefef;
    --paper: #ffffff;
    --charcoal: #5a5a5e;
    --orange: #f08a24;
    --sky: #29a3e0;
    --link-blue: #1b75c4;
    --text-grey: #666666;
    --flame-tint: #fdf1e4;
  }
  * { box-sizing: border-box; margin: 0; padding: 0; }
  html, body {
    width: 1006px; height: 1200px; overflow: hidden;
    background: var(--backdrop);
    font-family: "Open Sans", Arial, sans-serif;
  }
  .letterhead {
    position: absolute; left: 189px; top: 186px;
    width: 622px; height: 820px;
    background: var(--paper);
    box-shadow: 0 6px 14px rgba(0,0,0,0.18);
    overflow: hidden;
  }
  .top-bars { position: absolute; top: 0; left: 0; width: 100%; height: 10px; }
  .top-bars span { position: absolute; top: 0; height: 10px; }
  .bar-charcoal { left: 0; width: 158px; background: var(--charcoal); }
  .bar-orange { left: 161px; width: 230px; background: var(--orange); }
  .bar-sky { left: 395px; width: 227px; background: var(--sky); }

  .brand {
    position: absolute; left: 33px; top: 46px;
    display: flex; align-items: center; gap: 10px;
  }
  .brand-square { width: 34px; height: 34px; background: var(--charcoal); }
  .brand-name {
    font-weight: 600; font-size: 15px; line-height: 17px;
    color: var(--charcoal); text-transform: uppercase;
  }

  .contact {
    position: absolute; left: 393px; top: 42px;
    list-style: none; font-size: 10.5px; line-height: 13px;
    color: var(--text-grey);
  }
  .contact li { display: flex; align-items: center; gap: 5px; white-space: nowrap; }
  .contact svg { width: 8px; height: 9px; fill: var(--link-blue); }
  .contact .label { color: var(--link-blue); }

  .watermark {
    position: absolute; left: 160px; top: 270px;
    width: 300px; height: 410px;
    background: radial-gradient(ellipse at 50% 60%, var(--flame-tint) 0%, var(--flame-tint) 45%, rgba(253,241,228,0) 72%);
  }
  .footer-waves { position: absolute; left: 0; bottom: 0; width: 622px; height: 60px; }
</style>
</head>
<body>
  <main class="letterhead">
    <div class="top-bars">
      <span class="bar-charcoal"></span>
      <span class="bar-orange"></span>
      <span class="bar-sky"></span>
    </div>

    <header class="brand">
      <span class="brand-square"></span>
      <p class="brand-name">Gareth Whitfield<br>Plumbing</p>
    </header>

    <ul class="contact">
      <li><svg viewBox="0 0 8 10"><path d="M4 0a3.2 3.2 0 0 0-3.2 3.2C.8 5.6 4 10 4 10s3.2-4.4 3.2-6.8A3.2 3.2 0 0 0 4 0zm0 4.5a1.3 1.3 0 1 1 0-2.6 1.3 1.3 0 0 1 0 2.6z"/></svg>P.O Box 4826 Bega NSW 2550</li>
      <li><svg viewBox="0 0 8 10"><path d="M1.5 0h5a1 1 0 0 1 1 1v8a1 1 0 0 1-1 1h-5a1 1 0 0 1-1-1V1a1 1 0 0 1 1-1zm.3 1.2v6.6h4.4V1.2z"/></svg>0412076584</li>
      <li><svg viewBox="0 0 8 10"><path d="M0 2.5h8v5H0zM.6 3l3.4 2.4L7.4 3z" fill-rule="evenodd"/></svg>gareth@rwhitfieldplumbing.example.au</li>
      <li><span class="label">ABN</span>&nbsp;- 41 906 572 338</li>
      <li><span class="label">Licence No</span>&nbsp;- 582061K</li>
    </ul>

    <div class="watermark" role="img" aria-label="Faint brand decoration in pale orange"></div>

    <svg class="footer-waves" viewBox="0 0 622 60" preserveAspectRatio="none" aria-hidden="true">
      <path d="M0 22 C120 44 280 48 400 41 C500 35 560 32 622 32 L622 60 L0 60 Z" fill="var(--charcoal)"/>
      <path d="M0 4 C80 28 190 36 285 39 C190 40 80 34 0 17 Z" fill="var(--orange)"/>
      <path d="M340 32 C430 22 540 17 622 16 L622 28 C540 28 430 30 340 32 Z" fill="var(--sky)"/>
    </svg>
  </main>
</body>
</html>
```